2022 Landscaping Services

Please use the prior year design as an example. Similar style but DO NOT COPY IT EXACTLY- you can use different photos from our website if you like. Same text for year 2022.
Design should clearly depict the differences between the 3 products so people can buy one of them. Be creative!

size 8.5" x 11"

Must provide source file in photoshop if you are winner

Requirements
Must have
• Same text as original flier but with year 2022

```html
<!DOCTYPE html>
<html lang="en">
<head>
<meta charset="utf-8">
<title>Elmwood Cemetery – 2022 Gravesite Landscaping Packages</title>
<link href="https://fonts.googleapis.com/css2?family=Roboto:wght@400;500;700&family=Roboto+Condensed:wght@700&display=swap" rel="stylesheet">
<style>
:root{
  --bg:#5e5d5f;
  --paper:#ffffff;
  --red:#8e1212;
  --red-deep:#6e0a0a;
  --red-bright:#c41a1a;
  --ink:#1e1e1e;
  --row-light:#ececec;
  --row-gray-top:#f4f4f4;
  --row-gray-bot:#c9c9c9;
  --dark-top:#3a3a3a;
  --dark-bot:#0d0d0d;
  --tick-green:#a9dcae;
  --gold:#f3b240;
}
*{box-sizing:border-box;margin:0;padding:0}
html,body{width:959px;height:1200px;overflow:hidden;background:var(--bg);font-family:'Roboto',sans-serif;color:var(--ink)}
.flyer{position:absolute;left:16px;top:0;width:927px;height:1200px;background:var(--paper);overflow:hidden}
.hero{position:absolute;left:0;top:0;width:927px;height:469px}
.brand{position:absolute;left:0;top:60px;width:590px;display:flex;align-items:center;justify-content:center;gap:16px;color:var(--red)}
.brand-dot{width:26px;height:26px;border-radius:50%;border:2px solid var(--red)}
.brand-name{font-family:'Roboto',sans-serif;font-weight:500;font-size:34px;letter-spacing:1px;text-transform:uppercase}
.title{position:absolute;left:84px;top:190px;font-family:'Roboto Condensed',sans-serif;font-weight:700;color:#fff;font-size:57px;line-height:65px;text-transform:uppercase}
.backdrop{position:absolute;left:0;bottom:0;width:927px;height:180px;background:linear-gradient(#fff 0%,#e6e6e6 35%,#cfcfcf 100%)}
.table{position:absolute;left:29px;top:500px;width:869px;display:grid;grid-template-columns:216px 219px 218px 216px;grid-template-rows:83px repeat(6,70.5px) 85px;border-radius:22px;overflow:hidden;gap:0}
.cell{display:flex;align-items:center;justify-content:center;text-align:center;border-right:1px solid #fff;border-bottom:1px solid #fff}
.cell:nth-child(4n){border-right:none}
.head{background:linear-gradient(var(--red-bright) -40%,var(--red) 50%,var(--red-deep));color:#fff;font-weight:500;font-size:19px;line-height:23px;text-transform:uppercase;position:relative}
.head.services{justify-content:flex-start;padding-left:34px;text-align:left;font-family:'Roboto Condensed',sans-serif;font-weight:700;font-size:27px;line-height:34px}
.head.popular{padding-top:14px}
.badge{position:absolute;top:0;left:56px;width:102px;height:22px;background:linear-gradient(#ffd26a,var(--gold));border-radius:0 0 8px 8px;color:var(--red);font-weight:700;font-style:italic;font-size:12px;line-height:22px;text-transform:none}
.label{background:var(--row-light);justify-content:flex-start;text-align:left;padding-left:34px;font-weight:500;font-size:14.5px;line-height:18px;text-transform:uppercase}
.std{background:linear-gradient(var(--row-gray-top),var(--row-gray-bot))}
.dark{background:linear-gradient(var(--dark-top),var(--dark-bot));color:#fff}
.note{font-size:11.5px;line-height:14.5px;padding:0 10px}
.price{background:linear-gradient(var(--red-bright) -40%,var(--red) 50%,var(--red-deep));color:#fff;flex-direction:column;font-size:11.5px;line-height:14.5px;border-bottom:none}
.price.valid{align-items:flex-start;padding-left:34px;text-align:left;font-weight:500;font-size:19px;line-height:24px}
.amount{font-family:'Roboto Condensed',sans-serif;font-weight:700;font-size:21px;line-height:24px;margin-bottom:6px}
.terms{display:flex;margin-bottom:6px}
.term{padding:0 12px;font-weight:500;font-size:11px;line-height:14px}
.term+.term{border-left:1px solid #fff}
.contact{position:absolute;left:40px;top:1114px;width:850px;display:flex;align-items:center;gap:22px;font-weight:500;font-size:18px;line-height:22px}
.contact .item{display:flex;align-items:center;gap:8px}
.divider{width:1px;height:34px;background:#444}
.phone{color:var(--red);font-family:'Roboto Condensed',sans-serif;font-size:31px;font-weight:700}
.web b{color:var(--red);font-weight:500}
</style>
</head>
<body>
<div class="flyer">
  <div class="backdrop" role="img" aria-label="Soft grey silhouette of evergreen trees and a deer"></div>

  <svg class="hero" viewBox="0 0 927 469" aria-hidden="false">
    <defs>
      <linearGradient id="redBand" x1="0" y1="0" x2="1" y2="0">
        <stop offset="0" stop-color="#7a0c0c"/>
        <stop offset="1" stop-color="#d21b1b"/>
      </linearGradient>
      <linearGradient id="park" x1="0" y1="0" x2="0" y2="1">
        <stop offset="0" stop-color="#6f9a3c"/>
        <stop offset="0.55" stop-color="#4f7a2a"/>
        <stop offset="1" stop-color="#b9b9b4"/>
      </linearGradient>
    </defs>
    <polygon points="0,167 551,167 429,469 0,469" fill="url(#redBand)" role="img" aria-label="Red-tinted photo of a deer among headstones"/>
    <polygon points="619,0 927,0 927,469 429,469" fill="url(#park)" role="img" aria-label="Photo of tree-lined cemetery path with headstones and hedges"/>
    <polygon points="598,0 619,0 429,469 410,469" fill="#1a1a1a"/>
  </svg>

  <div class="brand">
    <span class="brand-name">Elmwood</span>
    <span class="brand-dot"></span>
    <span class="brand-name">Cemetery</span>
  </div>

  <h1 class="title">2022<br>Gravesite<br>Landscaping<br>Packages</h1>

  <svg width="0" height="0" style="position:absolute">
    <symbol id="ban" viewBox="0 0 30 30"><circle cx="15" cy="15" r="12.5" fill="none" stroke="#8e1212" stroke-width="2.4"/><line x1="6.5" y1="23.5" x2="23.5" y2="6.5" stroke="#8e1212" stroke-width="2.4"/></symbol>
    <symbol id="tick" viewBox="0 0 34 30"><path d="M2 16 L9 13 L14 22 Q22 8 33 1 Q22 12 14 29 Z"/></symbol>
  </svg>

  <div class="table">
    <div class="cell head services">Services<br>Offered</div>
    <div class="cell head">Seasonal Care<br>Endowment</div>
    <div class="cell head">Basic<br>Care Endowment</div>
    <div class="cell head popular"><span class="badge">Most Popular</span>Perpetual<br>Care Endowment</div>

    <div class="cell label">Weeding &amp; Trimming<br>on your gravesite</div>
    <div class="cell std note">Approximately every 7 weeks<br>during the growing season:<br>Mid-April through Mid-October</div>
    <div class="cell std note">2 times per year :<br>Mid-May &amp; Mid-September</div>
    <div class="cell dark note">Approximately every 7 weeks<br>during the growing season:<br>Mid-April through Mid-October</div>

    <div class="cell label">Payment ensured<br>forever grave care</div>
    <div class="cell std"><svg width="28" height="28"><use href="#ban"/></svg></div>
    <div class="cell std"><svg width="32" height="28" fill="#8e1212"><use href="#tick"/></svg></div>
    <div class="cell dark"><svg width="32" height="28" fill="var(--tick-green)"><use href="#tick"/></svg></div>

    <div class="cell label">Monument leveling</div>
    <div class="cell std"><svg width="28" height="28"><use href="#ban"/></svg></div>
    <div class="cell std"><svg width="32" height="28" fill="#8e1212"><use href="#tick"/></svg></div>
    <div class="cell dark"><svg width="32" height="28" fill="var(--tick-green)"><use href="#tick"/></svg></div>

    <div class="cell label">Monument cleaning</div>
    <div class="cell std"><svg width="28" height="28"><use href="#ban"/></svg></div>
    <div class="cell std"><svg width="28" height="28"><use href="#ban"/></svg></div>
    <div class="cell dark"><svg width="32" height="28" fill="var(--tick-green)"><use href="#tick"/></svg></div>

    <div class="cell label">Full bed of boxwood<br>shrubs</div>
    <div class="cell std"><svg width="28" height="28"><use href="#ban"/></svg></div>
    <div class="cell std"><svg width="28" height="28"><use href="#ban"/></svg></div>
    <div class="cell dark"><svg width="32" height="28" fill="var(--tick-green)"><use href="#tick"/></svg></div>

    <div class="cell label">Trust certificate</div>
    <div class="cell std"><svg width="28" height="28"><use href="#ban"/></svg></div>
    <div class="cell std"><svg width="28" height="28"><use href="#ban"/></svg></div>
    <div class="cell dark"><svg width="32" height="28" fill="var(--tick-green)"><use href="#tick"/></svg></div>

    <div class="cell price valid">Valid through<br>10/31/22</div>
    <div class="cell price">
      <div class="terms">
        <div class="term">$357<br>3 Years</div>
        <div class="term">$238<br>2 Years</div>
        <div class="term">$119<br>1 Years</div>
      </div>
      <div>Multi-year payment locks<br>in current rates</div>
    </div>
    <div class="cell price"><div class="amount">$255</div><div>12 Monthly payments.<br>Call for single payment discounts.</div></div>
    <div class="cell price"><div class="amount">$313</div><div>12 Monthly payments. Call for<br>single payment discounts.</div></div>
  </div>

  <div class="contact">
    <div class="item">
      <svg width="24" height="24" viewBox="0 0 24 24"><circle cx="12" cy="12" r="11" fill="none" stroke="#333" stroke-width="1.2"/><path d="M12 5a5 5 0 0 0-5 5c0 4 5 9 5 9s5-5 5-9a5 5 0 0 0-5-5z" fill="#b01515"/><circle cx="12" cy="10" r="1.8" fill="#fff"/></svg>
      <span>48 Orchard Lane,<br>Fairview Hills, NJ 07000</span>
    </div>
    <div class="divider"></div>
    <div class="item web">
      <svg width="24" height="24" viewBox="0 0 24 24"><circle cx="12" cy="12" r="11" fill="none" stroke="#333" stroke-width="1.2"/><circle cx="12" cy="12" r="6.5" fill="none" stroke="#b01515" stroke-width="1.4"/><ellipse cx="12" cy="12" rx="3" ry="6.5" fill="none" stroke="#b01515" stroke-width="1.2"/><line x1="5.5" y1="12" x2="18.5" y2="12" stroke="#b01515" stroke-width="1.2"/></svg>
      <span>www.<b>elmwoodmemorial</b>.org</span>
    </div>
    <div class="divider"></div>
    <div class="item">
      <svg width="24" height="24" viewBox="0 0 24 24"><circle cx="12" cy="12" r="11" fill="none" stroke="#333" stroke-width="1.2"/><path d="M8 6.5l2 .2 1 2.6-1.4 1.2a8 8 0 0 0 3.9 3.9l1.2-1.4 2.6 1 .2 2c-.1.7-.8 1.3-1.6 1.3A9.5 9.5 0 0 1 6.7 8.1c0-.8.6-1.5 1.3-1.6z" fill="#333"/></svg>
      <span class="phone">(555) 214-3090</span>
    </div>
  </div>
</div>
</body>
</html>
```